"Willow Drift" Mattress Pad Packaging

We need packaging for a mattress pad. This will be sold through retailers across North America. We need something modern and clean, an update from what we currently have. This is targeted towards older women. I've attached what our current packaging looks like as well as other mattress pad packaging. This is a simple product so we're open to creativity and experimentation. This is our first time using this site so we're very open and hoping for something fun.

Font styles to use
Serif
Sans Serif

Colors

Designer to choose colors to be used in the design.

```html
<!DOCTYPE html>
<html lang="en">
<head>
<meta charset="utf-8">
<title>Willow Drift – Mattress Pad Packaging Options</title>
<link rel="stylesheet" href="https://fonts.googleapis.com/css2?family=Cinzel:wght@400;500&display=swap">
<style>
  :root {
    --backdrop: #dfe4e6;
    --forest: #25582f;
    --forest-deep: #1d4826;
    --terracotta: #c9826b;
    --champagne: #ecd0b3;
    --badge: #1a1a1a;
    --badge-text: #ffffff;
  }
  * { margin: 0; padding: 0; box-sizing: border-box; }
  html, body {
    width: 1200px; height: 1165px; overflow: hidden;
    background: var(--backdrop);
  }
  .board { position: relative; width: 1200px; height: 1165px; }

  .option-badge {
    position: absolute; width: 50px; height: 50px; border-radius: 50%;
    background: var(--badge); color: var(--badge-text);
    font: 700 30px/50px Arial, Helvetica, sans-serif; text-align: center;
  }

  .label {
    position: absolute; width: 459px; height: 371px; overflow: hidden;
    background: var(--forest);
  }
  .label__pattern { position: absolute; inset: 0; background: radial-gradient(circle at 50% 40%, var(--forest) 0%, var(--forest-deep) 140%); }
  .label__frame { position: absolute; inset: 0; width: 100%; height: 100%; }

  .label__content {
    position: absolute; inset: 0; text-align: center; color: var(--champagne);
    font-family: "Cinzel", Georgia, serif;
  }
  .brand-mark {
    position: absolute; left: 50%; top: 62px; width: 50px; height: 50px;
    margin-left: -25px; border: 3px solid var(--champagne); border-radius: 50%;
  }
  .brand-name {
    position: absolute; left: 0; right: 0; top: 157px;
    font-size: 29px; font-weight: 400; letter-spacing: 1.5px; line-height: 1;
  }
  .brand-line {
    position: absolute; left: 0; right: 0; top: 193px;
    font-size: 11px; letter-spacing: 3px; line-height: 1;
  }
  .rating {
    position: absolute; left: 0; right: 0; top: 218px;
    font-family: Arial, sans-serif; font-size: 18px; letter-spacing: 2px; line-height: 1;
  }
  .divider {
    position: absolute; left: 120px; right: 120px; top: 228px; height: 1px;
    background: var(--champagne);
  }
  .divider::after {
    content: ""; position: absolute; left: 50%; top: -4px; width: 9px; height: 9px;
    margin-left: -4.5px; border-radius: 50%; background: var(--champagne);
  }
  .features {
    position: absolute; left: 0; right: 0; top: 253px; list-style: none;
    font-size: 12px; letter-spacing: 1.6px; line-height: 19px;
  }
</style>
</head>
<body>
<main class="board">

  <!-- Option 1 -->
  <span class="option-badge" style="left:64px;top:62px;">1</span>
  <section class="label" style="left:99px;top:157px;">
    <div class="label__pattern" role="img" aria-label="Repeating leaf-petal pattern in deep green"></div>
    <svg class="label__frame" viewBox="0 0 459 371" preserveAspectRatio="none" aria-hidden="true">
      <path d="M0 0 H36 Q66 185 36 371 H0 Z" fill="var(--terracotta)"/>
      <path d="M44 0 Q74 185 44 371" stroke="var(--terracotta)" stroke-width="3" fill="none"/>
      <path d="M459 0 H423 Q393 185 423 371 H459 Z" fill="var(--terracotta)"/>
      <path d="M415 0 Q385 185 415 371" stroke="var(--terracotta)" stroke-width="3" fill="none"/>
    </svg>
    <div class="label__content">
      <span class="brand-mark"></span>
      <h2 class="brand-name">Willow Drift</h2>
      <p class="brand-line">Haute Collection</p>
      <p class="rating">★★★★★</p>
      <ul class="features">
        <li>300 Thread Count</li>
        <li>Stretch-to-Fit-Skirt</li>
        <li>Allergy Deterrent</li>
        <li>100% Cotton</li>
      </ul>
    </div>
  </section>

  <!-- Option 2 -->
  <span class="option-badge" style="left:613px;top:62px;">2</span>
  <section class="label" style="left:648px;top:157px;">
    <div class="label__pattern" role="img" aria-label="Repeating leaf-petal pattern in deep green"></div>
    <svg class="label__frame" viewBox="0 0 459 371" preserveAspectRatio="none" aria-hidden="true">
      <rect x="19" y="0" width="7" height="371" fill="var(--terracotta)"/>
      <rect x="433" y="0" width="7" height="371" fill="var(--terracotta)"/>
    </svg>
    <div class="label__content">
      <span class="brand-mark"></span>
      <h2 class="brand-name">Willow Drift</h2>
      <p class="brand-line">Haute Collection</p>
      <span class="divider"></span>
      <ul class="features">
        <li>300 Thread Count</li>
        <li>Stretch-to-Fit-Skirt</li>
        <li>Allergy Deterrent</li>
        <li>100% Cotton</li>
      </ul>
    </div>
  </section>

  <!-- Option 3 -->
  <span class="option-badge" style="left:325px;top:605px;">3</span>
  <section class="label" style="left:356px;top:702px;">
    <div class="label__pattern" role="img" aria-label="Repeating leaf-petal pattern in deep green"></div>
    <svg class="label__frame" viewBox="0 0 459 371" preserveAspectRatio="none" aria-hidden="true">
      <path d="M26 0 Q72 185 26 371" stroke="var(--terracotta)" stroke-width="6" fill="none"/>
      <path d="M433 0 Q387 185 433 371" stroke="var(--terracotta)" stroke-width="6" fill="none"/>
    </svg>
    <div class="label__content">
      <span class="brand-mark"></span>
      <h2 class="brand-name">Willow Drift</h2>
      <p class="brand-line">Haute Collection</p>
      <p class="rating">★★★★★</p>
      <ul class="features">
        <li>300 Thread Count</li>
        <li>Stretch-to-Fit-Skirt</li>
        <li>Allergy Deterrent</li>
        <li>100% Cotton</li>
      </ul>
    </div>
  </section>

</main>
</body>
</html>
```